For Lease Sign to Attract National Retail Tenants

Attached is a logo design that was created by Pixel Harbor. I will like to develop a leasing sign that is 4 foot wide by 4 foot high or 4 feet wide and 6 feet high. I would like the sign to have a black background and use the colors that are in the logo. These will be signs that are placed in front of shopping centers and are often read by passing motorist so the sign must be simple, clean, very easy to read, distinctive, and have as few words as possible. It would be good if small amounts of bright green can be added as a boarder or ????? The text should be FOR LEASE, 555-283-7716, Reed Halvorsen. I will want to also design cards and letter head around the same theme.

Target Market(s)

National retail tenants wanting to lease space in my shopping centers

Industry/Entity Type

Real Estate Development

Contact Information for Business Card

Tall Oak RP, LLC Reed Halvorsen President & CEO 4172 Marrow Ave. Suite 305 Fenwick, CA 90000 555-283-7716 reedhalvorsen@mailbox.example

```html
<!DOCTYPE html>
<html lang="en">
<head>
<meta charset="utf-8">
<title>Tall Oak RP — For Lease Sign</title>
<link rel="stylesheet" href="https://fonts.googleapis.com/css2?family=Barlow+Condensed:wght@500;600&display=swap">
<style>
  :root {
    --backdrop: #34558f;
    --sign-black: #000000;
    --sign-green: #39b54a;
    --sign-red: #ec2834;
    --sign-silver: #d9d9d9;
  }
  html, body {
    margin: 0;
    padding: 0;
    width: 1200px;
    height: 1200px;
    overflow: hidden;
    background: var(--backdrop);
  }
  .lease-sign {
    display: block;
    width: 1200px;
    height: 1200px;
  }
  .sign-text {
    font-family: "Barlow Condensed", "Arial Narrow", sans-serif;
    font-weight: 600;
  }
  .brand-name { fill: var(--sign-silver); font-weight: 500; }
  .headline { fill: var(--sign-red); }
  .phone-number { fill: var(--sign-black); }
  .contact-name { fill: var(--sign-silver); font-weight: 500; }
</style>
</head>
<body>
<svg class="lease-sign" viewBox="0 0 1200 1200" xmlns="http://www.w3.org/2000/svg" role="img" aria-label="For lease sign: Tall Oak RP, LLC, For Lease, 555-283-7716, Reed Halvorsen">
  <!-- support posts -->
  <rect class="sign-post" x="248" y="1140" width="40" height="60" fill="var(--sign-black)"/>
  <rect class="sign-post" x="912" y="1140" width="40" height="60" fill="var(--sign-black)"/>

  <!-- sign panel -->
  <rect class="sign-panel" x="232" y="270" width="736" height="878" fill="var(--sign-black)"/>
  <rect class="sign-frame" x="247" y="285" width="706" height="848" fill="none" stroke="var(--sign-green)" stroke-width="3"/>

  <!-- brand name -->
  <text class="sign-text brand-name" x="600" y="388" font-size="64" text-anchor="middle" textLength="444" lengthAdjust="spacingAndGlyphs">TALL OAK RP, LLC</text>

  <!-- headline -->
  <text class="sign-text headline" x="600" y="644" font-size="200" text-anchor="middle" textLength="638" lengthAdjust="spacingAndGlyphs">FOR LEASE</text>

  <!-- phone band -->
  <rect class="phone-band" x="247" y="706" width="706" height="182" fill="var(--sign-green)"/>
  <text class="sign-text phone-number" x="600" y="844" font-size="137" text-anchor="middle" textLength="616" lengthAdjust="spacingAndGlyphs">555-283-7716</text>

  <!-- contact name -->
  <text class="sign-text contact-name" x="600" y="1028" font-size="103" text-anchor="middle" textLength="416" lengthAdjust="spacingAndGlyphs">REED HALVORSEN</text>
</svg>
</body>
</html>
```